Rest Bloom Soar: Mental Health Counseling brochure

I need a brochure that highlights my services. The inside panels should highlight: Individual therapy, Couples Therapy, Group Therapy and Psychotherapy in French. One other panels should include information on fees and insurance, and the second an "About me" panel. The final panel should be my contact ion.

You can pull all the text from my website and photos too. I am including files below that include shortened versions of the website text.

Business moto: Rest. Bloom Soar.
Your personal journey begins here.

Contact info is available on the web. A current address and a new address should be listed on the contact panel

Current location (until 12/23/2016): … 9address on website)
New Location (1/1/2017): 2424 Marbury Ave. NW, Suite 303
Washington DC 20016

Target Market(s)

professionals, adults, conservative. Men and women. Artsy photos. no stock photos.

Industry/Entity Type

Mental Health

Font styles to use
Sans Serif

Colors
33a6d7
33b8a4

Requirements
Must have
• no great gimmicks, something pretty, see my website. Text, photos or a photo from my website, my professional photo also from my website. www.MarissaTolvenLPC.example
• Calm, Artsy, elegant, young professionals, seasoned professionals.
Should not have
• no stock photos...

```html
<!DOCTYPE html>
<html lang="en">
<head>
<meta charset="utf-8">
<title>Rest Bloom Soar – Counseling Brochure</title>
<link href="https://fonts.googleapis.com/css2?family=Open+Sans:wght@400;600;700;800&family=Noto+Serif:ital@1&display=swap" rel="stylesheet">
<style>
  :root{
    --teal:#1592a9;
    --panel-light:#f2f2f3;
    --band-grey:#8d8f93;
    --ink:#1d1d1f;
    --white:#ffffff;
    --crop:#555;
  }
  *{margin:0;padding:0;box-sizing:border-box}
  html,body{width:1200px;height:961px;overflow:hidden;background:var(--white)}
  body{position:relative;font-family:"Open Sans",Arial,sans-serif;color:var(--ink)}
  .abs{position:absolute}
  .crop-mark{position:absolute;background:var(--crop)}
  .crop-v{width:1px;height:48px}
  .crop-h{height:1px;width:48px}

  .fees-panel{left:62px;top:62px;width:356px;height:440px;background:var(--panel-light)}
  .pill{position:absolute;border-radius:22px;display:flex;align-items:center;justify-content:center;font-weight:700;letter-spacing:.2px}
  .pill-fees{left:138px;top:114px;width:218px;height:43px;background:var(--teal);color:var(--white);font-size:16px}
  .body-copy{position:absolute;text-align:center;font-size:13.5px;line-height:16.8px}
  .body-copy p+p{margin-top:16.8px}
  .fees-copy{left:90px;top:182px;width:314px}

  .bio-band{left:62px;top:502px;width:356px;height:168px;background:var(--band-grey)}
  .portrait{left:169px;top:426px;width:150px;height:150px;border-radius:50%;border:3px solid var(--white);background:radial-gradient(circle at 50% 45%,#8a6b58 0,#5d4233 45%,#c9c7c3 75%);}
  .bio-title{left:62px;top:589px;width:356px;text-align:center;color:var(--white);font-weight:700;font-size:15px}
  .bio-lead{left:62px;top:612px;width:356px;text-align:center;color:var(--white);font-family:"Noto Serif",Georgia,serif;font-style:italic;font-size:15px;line-height:18px}
  .about-copy{left:90px;top:682px;width:314px}

  .contact-info{left:418px;top:182px;width:354px;text-align:center;font-size:13.5px;line-height:16.8px}
  .contact-info h3{font-size:13.5px;font-weight:700}
  .contact-info em{font-family:"Noto Serif",Georgia,serif;font-size:13px}
  .contact-info .gap{height:16.8px}
  .contact-info .web{font-weight:700}
  .pin{left:584px;top:120px}

  .contact-photo{left:418px;top:502px;width:354px;height:397px;background:linear-gradient(180deg,#9a9c9e 0%,#8a8682 28%,#6e5542 55%,#4c3324 80%,#2d1d13 100%)}
  .pill-contact{left:508px;top:566px;width:167px;height:42px;border:2px solid var(--white);color:var(--white);font-size:18px;font-weight:600;border-radius:21px}
  .quote{left:418px;top:764px;width:354px;text-align:center;color:var(--white);font-family:"Noto Serif",Georgia,serif;font-style:italic;font-size:18px;line-height:23px}

  .cover-photo{left:772px;top:62px;width:366px;height:608px;background:linear-gradient(180deg,#d9dcc4 0%,#86a391 30%,#6b8f86 55%,#3f5a66 78%,#1b2b40 100%)}
  .cover-name{left:772px;top:574px;width:366px;text-align:center;color:var(--white);font-weight:800;font-size:21px;letter-spacing:.3px}
  .tagline{left:772px;top:736px;width:366px;text-align:center}
  .tagline .motto{font-family:"Noto Serif",Georgia,serif;font-style:italic;font-size:22px;line-height:28px}
  .tagline .promise{font-weight:800;font-size:21px;line-height:27px}
</style>
</head>
<body>
  <div class="crop-mark crop-v" style="left:74px;top:0"></div>
  <div class="crop-mark crop-v" style="left:1126px;top:0"></div>
  <div class="crop-mark crop-v" style="left:74px;top:913px"></div>
  <div class="crop-mark crop-v" style="left:1126px;top:913px"></div>
  <div class="crop-mark crop-h" style="left:0;top:74px"></div>
  <div class="crop-mark crop-h" style="left:1152px;top:74px"></div>
  <div class="crop-mark crop-h" style="left:0;top:886px"></div>
  <div class="crop-mark crop-h" style="left:1152px;top:886px"></div>

  <section class="abs fees-panel"></section>
  <div class="pill pill-fees">FEES AND INSURANCE</div>
  <div class="body-copy fees-copy">
    <p>As a licensed professional counselor, my services qualify for partial reimbursement under most plans as an 'out of network' provider, not as a ‘participating’ or 'preferred' provider.</p>
    <p>My fees are considered within the 'usual and customary' range (UCR). If you wish to submit for reimbursement, I will provide you with the required information.</p>
    <p>Please check your coverage carefully by calling your insurer.</p>
  </div>

  <section class="abs bio-band"></section>
  <div class="abs portrait" role="img" aria-label="Professional portrait photo of the counselor"></div>
  <div class="abs bio-title">BIO</div>
  <div class="abs bio-lead">I am a Licensed Professional Counselor<br>practicing in DC and MD.</div>
  <div class="body-copy about-copy">
    <p>I have extensive experience working with individuals, couples and groups. I specialize in treating anxiety disorders, depression, adjustment issues, relationship issues, and thriving issues at work.</p>
    <p>Most of my clients are professionals, managers and executives in government, international organizations and the private sector.</p>
  </div>

  <svg class="abs pin" width="26" height="32" viewBox="0 0 26 32" aria-hidden="true">
    <path d="M13 1C6.4 1 1.5 6 1.5 12.3 1.5 20.5 13 31 13 31s11.5-10.5 11.5-18.7C24.5 6 19.6 1 13 1z" fill="var(--teal)"/>
    <circle cx="13" cy="12.5" r="5" fill="#fff"/>
  </svg>
  <div class="abs contact-info">
    <h3>CURRENT LOCATION</h3>
    <em>(until 12/23/2016)</em>
    <div>(202) 555-0148</div>
    <div>3150 Fenwick Ave., NW</div>
    <div>Suite 412</div>
    <div>Washington DC 20008</div>
    <div class="gap"></div>
    <h3>NEW LOCATION</h3>
    <em>(1/1/2017)</em>
    <div>2424 Marbury Ave. NW,</div>
    <div>Suite 303</div>
    <div>Washington DC 20016</div>
    <div class="gap"></div>
    <div class="web">E: marissa.tolven@example.com</div>
    <div class="web">www.marissatolvenlpc.example</div>
  </div>

  <div class="abs contact-photo" role="img" aria-label="Photo of a hiker walking through a sunlit mountain meadow"></div>
  <div class="pill pill-contact">CONTACT</div>
  <div class="abs quote">Discover the freedom and vitality<br>of being your true self!</div>

  <div class="abs cover-photo" role="img" aria-label="Photo of a person in a yoga pose on a cliff above a fjord"></div>
  <div class="abs cover-name">MARISSA TOLVEN, LPC</div>
  <div class="abs tagline">
    <div class="motto">Rest. Bloom Soar.</div>
    <div class="promise">YOUR PERSONAL JOURNEY<br>BEGINS HERE.</div>
  </div>
</body>
</html>
```